Pawn & Gun store business card design

Hello! We would like a new business card design for our pawn & gun store. We loan money on items of value and sell firearms, jewelry, electronics & more.

Card will need to have the following information:

Business name - Prairie Mint Pawn & Gun
Address - 2417 Cedar Bend Rd. Suite B Marlow Creek, TX 75431
Employees name - Carl Hembree
Phone number - 972-555-0183
Email - PrairieMintPawn@Mailvex.com
Website - PrairieMintPawn.com

Somewhere on the card we would like it to say "Offering 10 Month Layaway!" & "We buy & loan on anything of value!". Our main store color is orange (please see logo). Logo does not have to be on the business card but it can be. Would like the back to have an area to write a note on the back. We like vintage things like old coins, collectables, firearms and more so think about this in the design. We want a business card as unique as our store!

Colors

Designer to choose colors to be used in the design.

Requirements
Nice to have
• Vintage Style

```html
<!DOCTYPE html>
<html lang="en">
<head>
<meta charset="utf-8">
<title>Prairie Mint Pawn &amp; Gun – Business Card</title>
<link rel="stylesheet" href="https://fonts.googleapis.com/css2?family=Cinzel:wght@700;900&family=Lato:wght@400;700&display=swap">
<style>
  :root {
    --backdrop: #2f2f2f;
    --card: #ffffff;
    --band: #3a1d0b;
    --orange: #d9601f;
    --ink: #2a1608;
    --text: #3a3a3a;
    --ghost: #e6e6e6;
  }
  * { box-sizing: border-box; margin: 0; padding: 0; }
  html, body { width: 1200px; height: 866px; overflow: hidden; background: var(--backdrop); }
  .sheet {
    width: 1200px; height: 866px;
    display: flex; flex-direction: column; align-items: center; justify-content: center; gap: 26px;
  }
  .card {
    position: relative; width: 700px; height: 400px;
    background: var(--card); overflow: hidden;
    box-shadow: 0 6px 18px rgba(0,0,0,.45);
  }
  .band {
    position: absolute; left: 0; right: 0; bottom: 0; height: 86px;
    background: var(--band);
    display: flex; align-items: center; padding-left: 56px;
  }
  .tagline {
    font-family: "Cinzel", serif; font-weight: 700; font-size: 22px;
    color: var(--orange); letter-spacing: .5px;
  }
  /* front */
  .person { position: absolute; left: 56px; top: 70px; }
  .name {
    font-family: "Cinzel", serif; font-weight: 900; font-size: 30px;
    color: var(--ink); letter-spacing: 1px; margin-bottom: 18px;
  }
  .contact { list-style: none; font-family: "Lato", sans-serif; font-size: 19px; color: var(--text); }
  .contact li { display: flex; align-items: center; gap: 10px; line-height: 28px; }
  .contact svg { width: 16px; height: 16px; fill: var(--ink); flex: none; }
  .brand {
    position: absolute; right: 44px; top: 54px; width: 270px;
    display: flex; flex-direction: column; align-items: center; gap: 10px;
  }
  .brand-dot { width: 22px; height: 22px; border-radius: 50%; background: var(--orange); }
  .brand-name {
    font-family: "Cinzel", serif; font-weight: 900; font-size: 30px; line-height: 1.1;
    color: var(--orange); text-align: center;
  }
  .address {
    position: absolute; right: 56px; top: 214px;
    font-family: "Lato", sans-serif; font-size: 19px; line-height: 24px;
    color: var(--text); text-align: right;
  }
  /* back */
  .ghost-name {
    position: absolute; left: 0; right: 0; top: 100px;
    font-family: "Cinzel", serif; font-weight: 900; font-size: 78px;
    color: var(--ghost); text-align: center; letter-spacing: 2px;
  }
</style>
</head>
<body>
<main class="sheet">
  <section class="card card-front" aria-label="Card front">
    <div class="person">
      <h1 class="name">CARL HEMBREE</h1>
      <ul class="contact">
        <li><svg viewBox="0 0 16 16" aria-hidden="true"><path d="M3 1h3l1.5 4-2 1.3a9 9 0 0 0 4.2 4.2L11 8.5l4 1.5v3a2 2 0 0 1-2 2A12 12 0 0 1 1 3a2 2 0 0 1 2-2z"/></svg>972-555-0183</li>
        <li><svg viewBox="0 0 16 16" aria-hidden="true"><path d="M1 3h14v10H1zM2 4l6 5 6-5v-.5H2z" fill-rule="evenodd"/></svg>PrairieMintPawn@Mailvex.com</li>
        <li><svg viewBox="0 0 16 16" aria-hidden="true"><circle cx="8" cy="8" r="7"/></svg>PrairieMintPawn.com</li>
      </ul>
    </div>
    <div class="brand">
      <span class="brand-dot" aria-hidden="true"></span>
      <p class="brand-name">Prairie Mint Pawn &amp; Gun</p>
    </div>
    <p class="address">2417 Cedar Bend Rd.<br>Suite B Marlow Creek<br>TX 75431</p>
    <div class="band"><p class="tagline">OFFERING 10 MONTH LAYAWAY!</p></div>
  </section>

  <section class="card card-back" aria-label="Card back">
    <p class="ghost-name">PRAIRIE MINT</p>
    <div class="band"><p class="tagline">WE BUY &amp; LOAN ON ANYTHING OF VALUE!</p></div>
  </section>
</main>
</body>
</html>
```